Need updated stationery design for chiropractic clinic

We recently moved our office and are looking to refresh our letterhead, business cards, presentation folder and envelopes. I tend to prefer simple, clean designs. We communicate with a lot of attorneys and want to exude professionalism. I have attached our logo and 2 additional versions (all white and white letters instead of grey).

Target Market(s)

Other medical professionals and attorneys. Business cards will go to patients as well.

Industry/Entity Type

Healthcare

```html
<!DOCTYPE html>
<html lang="en">
<head>
<meta charset="utf-8">
<title>NorthSpine Care Letterhead</title>
<link rel="stylesheet" href="https://fonts.googleapis.com/css2?family=Lato:wght@400;700&family=Quicksand:wght@500&family=Great+Vibes&display=swap">
<style>
  :root {
    --backdrop: #e4e5e7;
    --paper: #ffffff;
    --ink: #262626;
    --brand: #1b9fc6;
    --band: #1597cf;
    --divider: #3fa6d6;
  }
  * { margin: 0; padding: 0; box-sizing: border-box; }
  html, body {
    width: 1200px; height: 1200px; overflow: hidden;
    background: var(--backdrop);
  }
  .letterhead {
    position: absolute; left: 221px; top: 50px;
    width: 758px; height: 1100px;
    background: var(--paper);
    box-shadow: 0 6px 24px rgba(0,0,0,0.18);
    overflow: hidden;
    font-family: "Lato", sans-serif;
    color: var(--ink);
  }
  .brand {
    position: absolute; left: 65px; top: 56px;
    display: flex; align-items: center; gap: 12px;
    color: var(--brand); font-family: "Lato", sans-serif; font-weight: 700;
  }
  .brand-mark { width: 30px; height: 30px; border-radius: 50%; background: var(--brand); flex: none; }
  .brand-name { font-size: 32px; line-height: 1; white-space: nowrap; }
  .contact {
    position: absolute; left: 525px; top: 42px;
    border-left: 1.5px solid var(--divider);
    padding-left: 9px;
    font-family: "Quicksand", sans-serif; font-weight: 500; font-style: normal;
    font-size: 12.5px; line-height: 18.5px; color: #333;
  }
  .contact-line { display: flex; align-items: center; gap: 5px; white-space: nowrap; }
  .contact-line svg { width: 10px; height: 10px; fill: var(--divider); flex: none; }
  .contact-gap { height: 3px; }
  .letter { position: absolute; left: 65px; width: 640px; font-size: 14.3px; line-height: 17.4px; }
  .date { top: 243px; font-size: 15px; }
  .recipient { top: 280px; font-size: 15px; line-height: 18.5px; }
  .company { top: 334px; font-size: 15px; line-height: 18.5px; }
  .salutation { top: 408px; font-size: 19px; font-weight: 700; }
  .body { top: 448px; letter-spacing: 0.1px; }
  .body p { text-align: justify; margin-bottom: 17px; }
  .closing { top: 756px; font-size: 14.5px; }
  .signature {
    top: 792px; font-family: "Great Vibes", cursive;
    font-size: 34px; line-height: 1.2; color: #1f1f1f;
  }
  .footer-rule {
    position: absolute; left: 65px; right: 65px; bottom: 58px;
    height: 1.5px; background: var(--divider);
  }
  .footer-band {
    position: absolute; left: 0; right: 0; bottom: 0;
    height: 40px; background: var(--band);
  }
</style>
</head>
<body>
  <main class="letterhead">
    <header>
      <div class="brand">
        <div class="brand-mark"></div>
        <div class="brand-name">NorthSpine Care</div>
      </div>
      <address class="contact">
        <div class="contact-line">P.O Box 4418-00210</div>
        <div class="contact-line">Kisumu, lakeview estate</div>
        <div class="contact-gap"></div>
        <div class="contact-line">
          <svg viewBox="0 0 10 10"><path d="M2 0.5 L3.8 0.5 L4.3 3 L3 3.8 Q4 6 6.2 7 L7 5.7 L9.5 6.2 L9.5 8 Q9.5 9.5 8 9.5 Q0.5 9 0.5 2 Q0.5 0.5 2 0.5 Z"/></svg>
          +254-118-4027
        </div>
        <div class="contact-line">
          <svg viewBox="0 0 10 10"><path d="M0.5 2 L9.5 2 L9.5 8.5 L0.5 8.5 Z M1.2 2.6 L5 5.6 L8.8 2.6 L8.8 3.4 L5 6.4 L1.2 3.4 Z" fill-rule="evenodd"/></svg>
          hello@northspinecare.com
        </div>
        <div class="contact-line">
          <svg viewBox="0 0 10 10"><circle cx="5" cy="5" r="4.5"/></svg>
          www.northspinecare.com
        </div>
      </address>
    </header>

    <div class="letter date">Feb-03-2022</div>
    <div class="letter recipient">Mr, Peter Alden<br>President</div>
    <div class="letter company">Harbor Legal Group<br>48 Ridge Road, Suite# 6<br>Town, State, 450017</div>
    <div class="letter salutation">Dear Mr, Peter</div>

    <div class="letter body">
      <p>Lorem ipsum dolor sit amet, consectetur adipisicing elit, sed do eiusmod tempor incididunt ut labore et dolore magna aliqua. Ut enim ad minim veniam, quis nostrud exercitation ullamco laboris nisi ut aliquip ex ea commodo consequat. Duis aute irure dolor in reprehenderit in voluptate velit esse cillum dolore eu fugiat nulla pariatur.</p>
      <p>Lorem ipsum dolor sit amet, consectetur adipisicing elit, sed do eiusmod tempor incididunt ut labore et dolore magna aliqua. Ut enim ad minim veniam, quis nostrud exercitation ullamco laboris nisi ut aliquip ex ea commodo consequat. Duis aute irure dolor in reprehenderit in voluptate velit esse cillum dolore eu fugiat nulla pariatur.</p>
      <p>Lorem ipsum dolor sit amet, consectetur adipisicing elit, sed do eiusmod tempor incididunt ut labore et dolore magna aliqua. Ut enim ad minim veniam, quis nostrud exercitation ullamco laboris nisi ut aliquip ex ea commodo consequat.</p>
      <p>Excepteur sint occaecat cupidatat non proident, sunt in culpa qui officia deserunt mollit anim id est laborum. re et dolore magnam aliquam quaerat voluptatem.</p>
    </div>

    <div class="letter closing">Regards</div>
    <div class="letter signature">Daniel Moreno</div>

    <div class="footer-rule"></div>
    <div class="footer-band"></div>
  </main>
</body>
</html>
```